Start up business website

IT Support provider that caters towards law enforcement / police departments. We'll offer remote IT support, backup / recovery services and cyber security. Will add updates soon.

Target Market(s)

Police departments / Law Enforcement

Coding

Coded - Design and coding required

Number of Pages Required

5+ page

Font styles to use
Other font styles liked:
• Use font style in uploaded logo

Colors
0054AA
0677BA
7BADD7
CADEEF
E8F1F8

```html
<!DOCTYPE html>
<html lang="en">
<head>
<meta charset="utf-8">
<title>Bastion Support Services</title>
<link href="https://fonts.googleapis.com/css2?family=Orbitron:wght@900&family=Roboto:wght@400;500;700&display=swap" rel="stylesheet">
<style>
:root{
  --blue:#0054AA;
  --blue-mid:#0677BA;
  --blue-light:#7BADD7;
  --blue-pale:#CADEEF;
  --blue-wash:#E8F1F8;
  --ink:#111111;
  --text:#555555;
  --white:#ffffff;
  --dark:#0d0e12;
}
*{margin:0;padding:0;box-sizing:border-box}
html,body{width:1200px;height:3658px;overflow:hidden}
body{position:relative;font-family:"Roboto",Arial,sans-serif;background:var(--white);color:var(--ink)}
.abs{position:absolute}
.display{font-family:"Orbitron","Roboto",sans-serif;font-weight:900;letter-spacing:2px}
.btn{position:absolute;display:flex;align-items:center;justify-content:center;gap:8px;background:var(--blue);color:var(--white);border-radius:30px;font-weight:700;text-transform:uppercase;font-size:16px}
.btn .arrow{width:15px;height:15px}

/* header */
.topline{left:0;top:0;width:1200px;height:4px;background:var(--blue)}
.header{left:0;top:4px;width:1200px;height:91px;background:var(--white)}
.brand{position:absolute;display:flex;align-items:center;gap:10px;font-family:"Roboto",sans-serif;font-weight:700;color:var(--blue)}
.brand .dot{border-radius:50%;background:var(--blue)}
.nav{position:absolute;right:112px;top:38px;display:flex;gap:33px;font-size:14px;font-weight:700;color:var(--ink)}

/* hero */
.hero{left:0;top:95px;width:1200px;height:695px;background:radial-gradient(circle at 990px 390px,#bfc2c7 0,#6b6e74 200px,#2a2b2f 420px,#0b0b0d 700px);}
.hero-title{left:112px;top:282px;font-size:54px;color:var(--white)}
.hero-text{left:112px;top:360px;width:410px;font-size:17px;line-height:27px;color:var(--white);font-weight:500}

/* about */
.about-name{left:111px;top:791px;width:420px;height:487px;display:flex;align-items:center;justify-content:center;font-size:60px;font-weight:700;color:var(--blue);letter-spacing:2px}
.section-title{font-size:37px}
.about-title{left:609px;top:847px;color:var(--ink)}
.about-title span{color:var(--blue)}
.about-copy{left:609px;top:916px;width:470px;font-size:14px;line-height:26.5px;color:var(--text)}
.about-copy p+p{margin-top:13px}

/* services */
.services{left:0;top:1318px;width:1200px;height:734px;background:linear-gradient(180deg,#0b4fa6,#0d56b3 50%,#0b4fa6)}
.services-title{left:0;width:1200px;top:1495px;text-align:center;color:var(--white)}
.service{position:absolute;top:1590px;width:320px;text-align:center;color:var(--white)}
.service h3{margin-top:34px;font-size:19px;font-weight:700}
.service p{margin-top:12px;font-size:14.5px;line-height:26px}
.badge{display:block;margin:0 auto;width:94px;height:108px}

/* blog */
.blog-title{left:0;width:1200px;top:2080px;text-align:center;color:var(--ink)}
.blog-title span{color:var(--blue)}
.card{position:absolute;top:2154px;width:309px;height:388px;background:var(--white);border-radius:8px;box-shadow:0 2px 14px rgba(0,0,0,.12);text-align:center}
.card .thumb{position:absolute;left:7px;top:7px;width:295px;height:203px;border-radius:6px}
.card .date{position:absolute;top:235px;width:100%;font-size:14px;color:var(--blue);font-weight:500}
.card h4{position:absolute;top:260px;width:100%;font-size:17px;font-weight:700;color:var(--ink)}
.card p{position:absolute;top:295px;left:20px;width:269px;font-size:14.5px;line-height:22px;color:var(--text)}
.card .more{position:absolute;top:356px;width:100%;font-size:15px;font-weight:700;color:var(--blue);display:flex;justify-content:center;align-items:center;gap:7px}

/* contact */
.contact{left:0;top:2599px;width:1200px;height:731px;background:radial-gradient(ellipse at 600px 480px,#2a2d33 0,#121317 55%,#0a0a0c 100%)}
.contact-title{left:0;width:1200px;top:2786px;text-align:center;color:var(--white)}
.field{position:absolute;border:2px solid var(--white);border-radius:28px;color:var(--white);font-size:14px;padding-left:28px;display:flex;align-items:center}
.field.area{border-radius:22px;align-items:flex-start;padding-top:22px}

/* footer */
.footer-col h5{font-size:18px;font-weight:500;color:var(--ink);margin-bottom:18px}
.footer-col li{list-style:none;font-size:13.5px;color:var(--text);height:33px;display:flex;align-items:flex-start;gap:10px}
.footer-col .chev{color:var(--blue);font-size:12px}
.social{position:absolute;width:36px;height:36px;border-radius:50%;background:#eceef1}
.rule{left:111px;top:3586px;width:978px;height:1px;background:#dddddd}
.copyright{left:0;width:1200px;top:3613px;text-align:center;font-size:13.5px;color:var(--text)}
.chat{left:1121px;top:3566px;width:38px;height:38px;border-radius:50%;background:var(--blue)}
</style>
</head>
<body>

<!-- Header -->
<div class="abs topline"></div>
<header class="abs header">
  <div class="brand" style="left:112px;top:26px;font-size:28px;letter-spacing:1px">
    <span class="dot" style="width:30px;height:30px"></span>BASTION
  </div>
  <nav class="nav">
    <span>HOME</span><span>ABOUT US</span><span>OUR SERVICES</span><span>RESOURCES</span><span>PRESS</span><span>CONTACT US</span>
  </nav>
</header>

<!-- Hero -->
<section class="abs hero" role="img" aria-label="Dark technology backdrop with circuit lines and a glowing radial interface"></section>
<svg class="abs" style="left:0;top:640px" width="1200" height="150" viewBox="0 0 1200 150">
  <polygon points="110,100 340,20 1200,105 1200,125 340,42 130,102" fill="#0b4fa6"/>
  <polygon points="0,150 0,145 340,42 1200,125 1200,150" fill="#ffffff"/>
</svg>
<h1 class="abs display hero-title">BASTION</h1>
<p class="abs hero-text">Lorem ipsum dolor sit amet, consectetur adipiscing elit, sed do eiusmod ut labore magna aliqua.</p>
<div class="btn" style="left:112px;top:440px;width:193px;height:47px">Get Started
  <svg class="arrow" viewBox="0 0 16 16"><circle cx="8" cy="8" r="8" fill="#fff"/><path d="M6.5 4.5 10 8l-3.5 3.5" stroke="#0054AA" stroke-width="2" fill="none"/></svg>
</div>

<!-- About -->
<div class="abs about-name">BASTION</div>
<h2 class="abs display section-title about-title">ABOUT <span>US</span></h2>
<div class="abs about-copy">
  <p>Lorem ipsum dolor sit amet, consectetur adipiscing elit, sed do eiusmod tempor incididunt ut labore et dolore magna aliqua. Ut enim ad minim veniam, quis nostrud exercitation ullamco laboris nisi ut aliquip ex ea commodo consequat. Duis aute irure dolor in reprehenderit in voluptate velit esse cillum dolore eu fugiat nulla pariatur.</p>
  <p>Lorem ipsum dolor sit amet, consectetur adipiscing elit, sed do eiusmod tempor incididunt ut labore et dolore magna aliqua. Ut enim ad minim commodo in irure voluptate reprehenderit in consequat.</p>
</div>
<div class="btn" style="left:609px;top:1173px;width:168px;height:44px;font-size:14px">Learn More
  <svg class="arrow" viewBox="0 0 16 16"><circle cx="8" cy="8" r="8" fill="#fff"/><path d="M6.5 4.5 10 8l-3.5 3.5" stroke="#0054AA" stroke-width="2" fill="none"/></svg>
</div>

<!-- Services -->
<section class="abs services" role="img" aria-label="Blue-tinted photo of officers on duty"></section>
<svg class="abs" style="left:0;top:1318px" width="1200" height="734" viewBox="0 0 1200 734">
  <polygon points="0,0 1200,0 1200,12 859,122 0,12" fill="#ffffff"/>
  <polygon points="0,30 859,125 1200,12 1200,30 859,148 0,52" fill="#111111" opacity=".9"/>
  <polygon points="0,700 340,600 1200,700 1200,734 0,734" fill="#ffffff"/>
  <polygon points="0,680 340,578 1200,690 1200,702 340,600 0,702" fill="#111111" opacity=".9"/>
</svg>
<h2 class="abs display section-title services-title">OUR SERVICES</h2>

<div class="service" style="left:104px">
  <svg class="badge" viewBox="0 0 94 108"><rect x="4" y="8" width="86" height="94" rx="20" fill="#fff"/>
    <circle cx="47" cy="42" r="11" fill="none" stroke="#0054AA" stroke-width="3"/><path d="M26 80c2-14 10-20 21-20s19 6 21 20" fill="none" stroke="#0054AA" stroke-width="3"/></svg>
  <h3>IT Support</h3>
  <p>Lorem ipsum dolor sit amet, consectetur adipiscing elit, do eiusmod tempor incididunt ut labore et dolore magna aliqua.</p>
</div>
<div class="service" style="left:439px">
  <svg class="badge" viewBox="0 0 94 108"><rect x="4" y="8" width="86" height="94" rx="20" fill="#fff"/>
    <path d="M27 52a20 20 0 0 1 36-12M67 56a20 20 0 0 1-36 12" fill="none" stroke="#0054AA" stroke-width="3"/><path d="M63 30v10H53M31 78V68h10" fill="none" stroke="#0054AA" stroke-width="3"/></svg>
  <h3>Recovery Services</h3>
  <p>Lorem ipsum dolor sit amet, consectetur adipiscing elit, do eiusmod tempor incididunt ut labore et dolore magna aliqua.</p>
</div>
<div class="service" style="left:774px">
  <svg class="badge" viewBox="0 0 94 108"><rect x="4" y="8" width="86" height="94" rx="20" fill="#fff"/>
    <rect x="24" y="32" width="46" height="32" rx="3" fill="none" stroke="#0054AA" stroke-width="3"/><path d="M47 64v10M36 76h22" stroke="#0054AA" stroke-width="3"/><circle cx="47" cy="46" r="5" fill="none" stroke="#0054AA" stroke-width="3"/></svg>
  <h3>Cyber Security</h3>
  <p>Lorem ipsum dolor sit amet, consectetur adipiscing elit, do eiusmod tempor incididunt ut labore et dolore magna aliqua.</p>
</div>

<!-- Blog -->
<h2 class="abs display section-title blog-title"><span>OUR</span> BLOG</h2>

<article class="card" style="left:111px">
  <div class="thumb" role="img" aria-label="Hands typing on a laptop with a glowing lock overlay" style="background:linear-gradient(135deg,#0a1c3e,#1d4f9a 60%,#6fa3dc)"></div>
  <div class="date">▦ February 2, 2021</div>
  <h4>Lorem ipsum dolor sit amet,</h4>
  <p>Sed ut perspiciatis unde omnis iste natus sit voluptatem accusantium</p>
  <div class="more">READ MORE <svg width="14" height="14" viewBox="0 0 16 16"><circle cx="8" cy="8" r="8" fill="#0054AA"/><path d="M6.5 4.5 10 8l-3.5 3.5" stroke="#fff" stroke-width="2" fill="none"/></svg></div>
</article>
<article class="card" style="left:446px">
  <div class="thumb" role="img" aria-label="Officer standing in front of a patrol car" style="background:linear-gradient(160deg,#d9dde3,#8c939d 50%,#2a2d33)"></div>
  <div class="date">▦ February 2, 2021</div>
  <h4>Lorem ipsum dolor sit amet,</h4>
  <p>Sed ut perspiciatis unde omnis iste natus sit voluptatem accusantium</p>
  <div class="more">READ MORE <svg width="14" height="14" viewBox="0 0 16 16"><circle cx="8" cy="8" r="8" fill="#0054AA"/><path d="M6.5 4.5 10 8l-3.5 3.5" stroke="#fff" stroke-width="2" fill="none"/></svg></div>
</article>
<article class="card" style="left:780px">
  <div class="thumb" role="img" aria-label="Analyst holding a tablet in a server monitoring room" style="background:linear-gradient(135deg,#1a2f55,#3d6fae 55%,#9cc2e6)"></div>
  <div class="date">▦ February 2, 2021</div>
  <h4>Lorem ipsum dolor sit amet,</h4>
  <p>Sed ut perspiciatis unde omnis iste natus sit voluptatem accusantium</p>
  <div class="more">READ MORE <svg width="14" height="14" viewBox="0 0 16 16"><circle cx="8" cy="8" r="8" fill="#0054AA"/><path d="M6.5 4.5 10 8l-3.5 3.5" stroke="#fff" stroke-width="2" fill="none"/></svg></div>
</article>

<!-- Contact -->
<section class="abs contact" role="img" aria-label="Dark backdrop with a flowing wave of glowing particles"></section>
<svg class="abs" style="left:0;top:2599px" width="1200" height="731" viewBox="0 0 1200 731">
  <polygon points="0,0 1200,0 1200,12 859,115 0,0" fill="#ffffff"/>
  <polygon points="0,0 859,115 1200,12 1200,30 859,132 0,18" fill="#0b4fa6"/>
  <polygon points="0,731 0,715 340,603 1200,700 1200,731" fill="#ffffff"/>
  <polygon points="110,690 340,600 1200,685 1200,700 340,618 130,692" fill="#0b4fa6"/>
</svg>
<h2 class="abs display section-title contact-title">CONTACT US</h2>
<div class="field" style="left:190px;top:2868px;width:394px;height:53px">Name</div>
<div class="field" style="left:190px;top:2934px;width:394px;height:53px">Email Address</div>
<div class="field" style="left:190px;top:2999px;width:394px;height:53px">Phone Number</div>
<div class="field area" style="left:606px;top:2866px;width:398px;height:187px">Message</div>
<div class="btn" style="left:497px;top:3096px;width:206px;height:51px">Submit Now
  <svg class="arrow" viewBox="0 0 16 16"><circle cx="8" cy="8" r="8" fill="#fff"/><path d="M6.5 4.5 10 8l-3.5 3.5" stroke="#0054AA" stroke-width="2" fill="none"/></svg>
</div>

<!-- Footer -->
<div class="brand" style="left:111px;top:3392px;font-size:34px;letter-spacing:1px">
  <span class="dot" style="width:38px;height:38px"></span>BASTION
</div>
<span class="social" style="left:148px;top:3487px" aria-label="Social profile"></span>
<span class="social" style="left:191px;top:3487px" aria-label="Social profile"></span>
<span class="social" style="left:234px;top:3487px" aria-label="Social profile"></span>
<span class="social" style="left:277px;top:3487px" aria-label="Social profile"></span>

<div class="abs footer-col" style="left:452px;top:3356px">
  <h5>Quick Links</h5>
  <ul><li><span class="chev">»</span>Home</li><li><span class="chev">»</span>About Us</li><li><span class="chev">»</span>Services</li><li><span class="chev">»</span>Careers</li><li><span class="chev">»</span>Resource</li></ul>
</div>
<div class="abs footer-col" style="left:656px;top:3356px">
  <h5>Important</h5>
  <ul><li style="margin-top:4px"><span class="chev">»</span>Terms of Use</li><li><span class="chev">»</span>Site Map</li><li><span class="chev">»</span>Privacy Policy</li><li><span class="chev">»</span>Disclaimer</li></ul>
</div>
<div class="abs footer-col" style="left:863px;top:3356px">
  <h5>Contact us</h5>
  <ul>
    <li style="height:50px;margin-top:4px;line-height:24px"><svg width="12" height="14" viewBox="0 0 12 14" style="margin-top:5px;flex:none"><path d="M6 14S1 8 1 5a5 5 0 0 1 10 0c0 3-5 9-5 9z" fill="#0054AA"/><circle cx="6" cy="5" r="2" fill="#fff"/></svg><span>48 Harbor Lane, Westfield,<br>Ohio, USA</span></li>
    <li><svg width="12" height="14" viewBox="0 0 12 14" style="flex:none"><rect x="2" y="0" width="8" height="14" rx="1.5" fill="#0054AA"/><rect x="3.5" y="2" width="5" height="8" fill="#fff"/></svg>+1 614-555-0142</li>
    <li><svg width="14" height="14" viewBox="0 0 14 14" style="flex:none"><rect x="0" y="3" width="14" height="10" rx="1.5" fill="#0054AA"/><rect x="3" y="0" width="8" height="4" fill="#0054AA"/></svg>+1 614-555-0187</li>
    <li><svg width="14" height="12" viewBox="0 0 14 12" style="flex:none"><rect x="1" y="1" width="12" height="10" fill="none" stroke="#0054AA" stroke-width="1.5"/><path d="M1 1l6 5 6-5" fill="none" stroke="#0054AA" stroke-width="1.5"/></svg>info@bastionsupport.com</li>
  </ul>
</div>
<div class="abs rule"></div>
<p class="abs copyright">© 2021 &nbsp;Bastion &nbsp;| &nbsp;All Rights Reserved</p>
<div class="abs chat" aria-label="Chat">
  <svg width="38" height="38" viewBox="0 0 38 38"><path d="M11 13h16v10H17l-4 4v-4h-2z" fill="#fff"/><circle cx="15" cy="18" r="1.3" fill="#0054AA"/><circle cx="19" cy="18" r="1.3" fill="#0054AA"/><circle cx="23" cy="18" r="1.3" fill="#0054AA"/></svg>
</div>

</body>
</html>
```